Commercial Piping Company Needs A Modern Business Card

We need a clean business card for our commercial pipe lining company. We would like to see a mock up in two color schemes: Black, Grey and Blue and Black, Grey and Orange. We are in the piping industry, but want a professional, clean and modern look to the card.

Industry/Entity Type

Plumbing

Contact Information for Business Card

Name: Mark Tollen
Title: Managing Partner
Phone: 382.615.9073
Email: Mark@VantoPipe.Net

Requirements
Must have
• Back Side Should Have a White Back Ground with Full Logo. Front I would like to see a couple lay outs for contact info. Also the final card will have rounded edges, so please take that into account for printing.
Nice to have
• Two Color Palette Examples
Should not have
• No need for an address line

```html
<!DOCTYPE html>
<html lang="en">
<head>
<meta charset="utf-8">
<title>VantoPipe Business Card</title>
<link href="https://fonts.googleapis.com/css2?family=Lato:wght@400;700&display=swap" rel="stylesheet">
<style>
  :root {
    --stage: #3a3a3a;
    --card-dark: #1f1f20;
    --emboss: #3b3b3d;
    --emboss-light: #4a4a4c;
    --card-light: #ffffff;
    --ink: #111111;
    --blue: #1a56a8;
  }
  * { margin: 0; padding: 0; box-sizing: border-box; }
  html, body { width: 1200px; height: 912px; overflow: hidden; }
  body {
    background: var(--stage);
    font-family: "Lato", sans-serif;
    display: flex; flex-direction: column; align-items: center; justify-content: center;
    gap: 40px;
  }
  .card {
    width: 700px; height: 400px; border-radius: 34px;
    display: flex; align-items: center; justify-content: center;
    box-shadow: 0 10px 30px rgba(0,0,0,0.45);
  }
  .card--back { background: var(--card-dark); }
  .card--front { background: var(--card-light); }

  .logo { display: flex; align-items: center; gap: 18px; }
  .logo__mark { border-radius: 50%; flex: none; }
  .logo__name { font-weight: 400; line-height: 1; }

  .card--back .logo__mark { width: 110px; height: 110px; background: var(--emboss); }
  .card--back .logo__name { font-size: 60px; color: var(--emboss-light); }

  .card--front .logo__mark { width: 70px; height: 70px; background: var(--ink); }
  .card--front .logo__name { font-size: 34px; color: var(--ink); }

  .divider { width: 2px; height: 150px; background: var(--blue); margin: 0 36px; }

  .contact { color: var(--ink); }
  .contact__name { font-size: 28px; font-weight: 700; color: var(--blue); }
  .contact__title { font-size: 17px; margin: 4px 0 16px 20px; }
  .contact__row { display: flex; align-items: center; gap: 10px; font-size: 18px; margin: 4px 0 0 20px; }
  .contact__row svg { width: 16px; height: 16px; fill: var(--blue); flex: none; }
</style>
</head>
<body>
  <section class="card card--back">
    <div class="logo">
      <div class="logo__mark"></div>
      <div class="logo__name">VantoPipe</div>
    </div>
  </section>

  <section class="card card--front">
    <div class="logo">
      <div class="logo__mark"></div>
      <div class="logo__name">VantoPipe</div>
    </div>
    <div class="divider"></div>
    <div class="contact">
      <div class="contact__name">Mark Tollen</div>
      <div class="contact__title">Managing Partner</div>
      <div class="contact__row">
        <svg viewBox="0 0 24 24" aria-hidden="true"><path d="M6.6 10.8a15.1 15.1 0 0 0 6.6 6.6l2.2-2.2a1 1 0 0 1 1-.25 11.4 11.4 0 0 0 3.6.57 1 1 0 0 1 1 1V20a1 1 0 0 1-1 1A17 17 0 0 1 3 4a1 1 0 0 1 1-1h3.5a1 1 0 0 1 1 1c0 1.25.2 2.45.57 3.57a1 1 0 0 1-.25 1z"/></svg>
        <span>382.615.9073</span>
      </div>
      <div class="contact__row">
        <svg viewBox="0 0 24 24" aria-hidden="true"><path d="M2 5h20v14H2z M2 5l10 8 10-8" fill="none" stroke="#1a56a8" stroke-width="2"/><path d="M2 5h20l-10 8z"/></svg>
        <span>Mark@VantoPipe.Net</span>
      </div>
    </div>
  </section>
</body>
</html>
```